Owen Partridge - Sales Executive Resume (need overhaul)

Executive Sales Rep (Cybersecurity) in need of an resume overhaul. One pager is preferred length but open to ideas. Been a long time since I've had to provide a resume. I've uploaded the resume with the standard content that could be leveraged but also looking for ideas on how to be more concise, and/or draw out key strengths.

Target Market(s)

Cybersecurity providers, Cloud Service Providers, System Integrators, Government Contractors

Industry/Entity Type

Commercial

Font styles to use
Sans Serif
Other font styles liked:
• designer choice (surprise me)

Colors
0393ce

Requirements
Must have
• -Be unique - ability to catch someone's attention at first glance
• -Ability to showcase business impacts in my career.
• -Content updates (emphasize business value/impact)
• -Highlight Key Skills/Cert's (CISSP, PMP, Brightmoor Sales Training, etc..)
Nice to have
• -Help with messaging on content
Should not have
• -too much narrative. Its been a while since I've created a resume. I need someone to help me make this modern, edgy, succinct.

```html
<!DOCTYPE html>
<html lang="en">
<head>
<meta charset="utf-8">
<title>Owen Partridge – Sales Executive Resume</title>
<link href="https://fonts.googleapis.com/css2?family=Open+Sans:wght@400;600;700&family=Questrial&display=swap" rel="stylesheet">
<style>
  :root {
    --backdrop: #d6d8de;
    --page: #f3f3f3;
    --panel: #cde0ee;
    --ink: #1b1b1b;
    --text: #555a60;
    --muted: #6a6f75;
    --teal: #0e5570;
    --date: #1a78b4;
    --side-head: #4a78b6;
    --dot-on: #3d74c0;
    --dot-off: #b9c9d8;
    --ring: #aab8c6;
    --footer: #555555;
  }
  * { box-sizing: border-box; margin: 0; padding: 0; }
  html, body { width: 1200px; height: 896px; overflow: hidden; }
  body { background: var(--backdrop); font-family: 'Open Sans', sans-serif; }

  .resume {
    position: absolute; left: 287px; top: 34px;
    width: 603px; height: 837px;
    background: var(--page);
    box-shadow: 0 4px 18px rgba(0,0,0,.18);
    overflow: hidden;
  }
  .abs { position: absolute; }

  /* Sidebar */
  .sidebar { left: 0; top: 105px; width: 205px; height: 693px; background: var(--panel); }
  .portrait {
    left: 60px; top: 56px; width: 89px; height: 89px; border-radius: 50%;
    background: radial-gradient(circle at 50% 40%, #8d8d8d, #3c3c3c 70%);
    border: 2px solid #eef3f7; box-shadow: 0 0 0 1px #c5d3df;
  }
  .side-head {
    font-family: 'Questrial', sans-serif; color: var(--side-head);
    font-size: 11.5px; line-height: 14px; height: 14px;
  }
  .side-head .label { position: absolute; top: 0; white-space: nowrap; }
  .side-head svg { position: absolute; top: 0; width: 13px; height: 13px; fill: var(--ink); }
  .side-head.spaced .label { letter-spacing: 3px; }
  .profile-text {
    left: 38px; top: 204px; width: 151px;
    font-family: 'Questrial', sans-serif; font-size: 7px; line-height: 9px;
    color: #3f444a; text-align: justify;
  }
  .skills { left: 38px; top: 399px; width: 138px; font-family: 'Questrial', sans-serif; font-size: 7.2px; color: #3f444a; }
  .skill-row { position: relative; height: 13px; line-height: 13px; white-space: nowrap; }
  .dots { position: absolute; left: 99px; top: 4px; display: flex; gap: 4.8px; }
  .dots i { width: 4.5px; height: 4.5px; border-radius: 50%; background: var(--dot-off); display: block; }
  .dots i.on { background: var(--dot-on); }
  .lang {
    width: 62px; height: 62px; border-radius: 50%;
    border: 2px solid var(--ring);
    display: flex; align-items: center; justify-content: center;
    font-weight: 600; font-size: 9px; color: var(--side-head);
  }
  .lang.strong { border-color: #96a6b6; }

  /* Header */
  .name { left: 264px; top: 66px; font-size: 33px; line-height: 40px; color: var(--ink); font-weight: 400; letter-spacing: .3px; white-space: nowrap; }
  .name strong { color: var(--teal); font-weight: 600; }
  .role { left: 265px; top: 103px; font-size: 8.2px; line-height: 10px; letter-spacing: 2.4px; color: var(--date); }

  /* Main sections */
  .section-head { color: var(--teal); font-size: 13px; line-height: 16px; font-weight: 400; white-space: nowrap; }
  .section-icon { width: 13px; height: 13px; }
  .timeline { left: 267px; top: 184px; width: 1px; height: 442px; background: #9aa0a6; }
  .node { left: 265px; width: 5px; height: 5px; border-radius: 50%; background: var(--ink); }
  .date { left: 220px; font-size: 6.8px; line-height: 8.3px; color: var(--date); white-space: nowrap; }
  .entry { left: 290px; width: 231px; }
  .entry h3 { font-size: 8.4px; font-weight: 700; color: #4a4f55; line-height: 10px; white-space: nowrap; }
  .entry .org { font-size: 8px; color: var(--muted); line-height: 10px; white-space: nowrap; }
  .entry p, .entry ul { font-size: 6.9px; line-height: 8.3px; color: var(--text); text-align: justify; }
  .entry ul { list-style: none; }
  .entry li::before { content: "•"; display: inline-block; width: 36px; }
  .loc { left: 510px; display: flex; align-items: center; gap: 6px; font-size: 8.2px; line-height: 10px; color: var(--muted); white-space: nowrap; }
  .loc svg { width: 5px; height: 7px; fill: var(--ink); }

  .contact-row { left: 264px; display: flex; align-items: center; height: 12px; font-size: 8.2px; color: var(--muted); white-space: nowrap; }
  .contact-row svg { width: 9px; height: 9px; fill: #3a3d41; flex: none; margin-right: 19px; }

  .footer-bar { left: 38px; top: 823px; width: 473px; height: 14px; background: var(--footer); }
</style>
</head>
<body>
<main class="resume">

  <aside class="abs sidebar" aria-label="Sidebar"></aside>
  <div class="abs portrait" role="img" aria-label="Portrait photo of Owen Partridge"></div>

  <!-- Profile -->
  <h2 class="abs side-head spaced" style="left:38px;top:170px;width:120px;">
    <svg style="left:0" viewBox="0 0 16 16"><circle cx="8" cy="4.5" r="3.5"/><path d="M1 15c0-4 3-6 7-6s7 2 7 6z"/></svg>
    <span class="label" style="left:21px;">PROFILE</span>
  </h2>
  <p class="abs profile-text">Forward-thinking Senior Executive with a proven cloud and cyber record with an early-stage company business achievement supporting a broad range of public and private sector security initiatives public (Federal, Defense) and private sector (Fortune 500) organizations. Articulate communicator with strong interpersonal and negotiating skills honed from supporting large system integrator contracts and industry leading cloud providers. Acute focus on hyperscale cloud providers and ecosystem partners where emerging cloud technologies and cyber security intersect.</p>

  <!-- Skills -->
  <h2 class="abs side-head" style="left:38px;top:367px;width:120px;">
    <svg style="left:0" viewBox="0 0 16 16" fill="none" stroke="#1b1b1b" stroke-width="1.3"><path d="M1 1v14h14"/><path d="M3 12l3-4 3 2 4-6"/></svg>
    <span class="label" style="left:27px;">SKILLS</span>
  </h2>
  <div class="abs skills">
    <div class="skill-row">PMP (1370452)<span class="dots"><i class="on"></i><i class="on"></i><i class="on"></i><i></i><i></i></span></div>
    <div class="skill-row">CISSP (318205)<span class="dots"><i class="on"></i><i class="on"></i><i class="on"></i><i></i><i></i></span></div>
    <div class="skill-row">Nimbus Solutions Architect<span class="dots"><i class="on"></i><i class="on"></i><i class="on"></i><i></i><i></i></span></div>
    <div class="skill-row">Associate (In Progress)</div>
  </div>

  <!-- Languages -->
  <h2 class="abs side-head" style="left:38px;top:490px;width:120px;">
    <svg style="left:0" viewBox="0 0 16 16"><path d="M1 2h13l-3 4 3 4H4l2 5H4L1 3z"/></svg>
    <span class="label" style="left:27px;">LANGUAGES</span>
  </h2>
  <div class="abs lang" style="left:40px;top:532px;">ENGLISH</div>
  <div class="abs lang strong" style="left:112px;top:532px;">GERMAN</div>

  <!-- Header -->
  <h1 class="abs name">OWEN <strong>PARTRIDGE</strong></h1>
  <div class="abs role">SALES EXECUTIVE</div>

  <!-- Work experience -->
  <svg class="abs section-icon" style="left:259px;top:168px;" viewBox="0 0 16 16" fill="none" stroke="#1b1b1b" stroke-width="1.2"><rect x="1.5" y="4.5" width="13" height="10"/><path d="M5.5 4.5V2h5v2.5M1.5 8.5h13M7 8v2h2V8"/></svg>
  <h2 class="abs section-head" style="left:290px;top:169px;">WORK EXPERIENCE</h2>
  <div class="abs timeline"></div>

  <div class="abs node" style="top:215px;"></div>
  <div class="abs date" style="top:214px;">2015 –<br>2018</div>
  <div class="abs entry" style="top:212px;">
    <h3>VP, GLOBAL ACCOUNTS</h3>
    <div class="org">Emberline Systems, Westminster</div>
    <ul style="margin-top:10px;">
      <li>Generated 100 million dollars in pipeline in 6 months for cloud hyperscale providers through strategic marketing efforts (content campaigns, thought leadership and workshops)</li>
      <li>Increased average company deal size from $35k to $200k security services in less than 2 years through advanced problem solving and deal packaging</li>
      <li>Heavily involved in building and advancing Emberline</li>
    </ul>
  </div>
  <div class="abs loc" style="top:220px;"><svg viewBox="0 0 10 14"><path d="M0 0h10v8l-5 6-5-6z"/></svg>Colorado</div>

  <div class="abs node" style="top:313px;"></div>
  <div class="abs date" style="top:309px;">2012-10 -<br>2016-12</div>
  <div class="abs entry" style="top:310px;">
    <h3>VP, STRATEGIC PARTNERSHIPS</h3>
    <p style="margin-top:9px;">VP, Strategic Partnerships (2012-2016)<br>-Consistent delivery of sales targets and long term account strategy (met or exceeded targets all 4 years)<br>-Lead the organization in building out an Nimbus Partnership level to Advanced w/ several competencies (built operational and sales</p>
  </div>
  <div class="abs loc" style="top:315px;"><svg viewBox="0 0 10 14"><path d="M0 0h10v8l-5 6-5-6z"/></svg>VA</div>

  <div class="abs node" style="top:385px;"></div>
  <div class="abs date" style="top:382px;">Jul 2014-<br>Nov 2014</div>
  <div class="abs entry" style="top:382px;">
    <h3>SENIOR PROJECT MANAGER</h3>
    <div class="org" style="font-size:7px;">Veritrex Incorporated</div>
    <p style="margin-top:6px;">Senior Project Manager (2008-2009)<br>-Lead a FISMA compliance team in support of 100 medical centers across Veterans Affairs (FISMA documentation/technical validation support)<br>-Supported business development activities across the company (proposal creation, technical approach, color reviews)</p>
  </div>
  <div class="abs loc" style="top:387px;"><svg viewBox="0 0 10 14"><path d="M0 0h10v8l-5 6-5-6z"/></svg>Reston, VA</div>

  <div class="abs node" style="top:472px;"></div>
  <div class="abs date" style="top:471px;left:221px;">Jun 2013-<br>May 2014</div>
  <div class="abs entry" style="top:470px;">
    <h3>SR. SECURITY ENGINEER</h3>
    <div class="org">Redpeak eSports</div>
    <p style="margin-top:7px;">Stratus Federal Systems, Sterling, VA<br>Security Engineer<br>-Conducted security audits (FISMA, other) on traditional IT and cloud based enterprises.<br>-Developed the facilities clearance plan for successfully submitting Performed risk analyses to identify appropriate security counter-measures.</p>
  </div>
  <div class="abs loc" style="top:474px;"><svg viewBox="0 0 10 14"><path d="M0 0h10v8l-5 6-5-6z"/></svg>Sterling, VA</div>

  <!-- Education -->
  <svg class="abs section-icon" style="left:257px;top:576px;" viewBox="0 0 16 16" fill="none" stroke="#1b1b1b" stroke-width="1.3"><path d="M8 4v11M1.5 3.5h6.5v11H1.5zM8 3.5h6.5v11H8z"/></svg>
  <h2 class="abs section-head" style="left:287px;top:574px;">EDUCATION</h2>
  <div class="abs timeline" style="top:592px;height:28px;"></div>
  <div class="abs node" style="top:619px;"></div>
  <div class="abs date" style="top:617px;">1994-09 -<br>1999-01</div>
  <div class="abs entry" style="top:616px;width:215px;">
    <h3>BACHELOR OF SCIENCE: SPORTS MANAGEMENT</h3>
    <div class="org">Meridian University - Lynchburg, VA</div>
  </div>
  <div class="abs loc" style="top:620px;"><svg viewBox="0 0 10 14"><path d="M0 0h10v8l-5 6-5-6z"/></svg>Missouri</div>

  <!-- Contacts -->
  <h2 class="abs section-head" style="left:289px;top:679px;color:var(--side-head);font-size:11.5px;">CONTACTS</h2>
  <div class="abs contact-row" style="top:706px;"><svg viewBox="0 0 16 16"><path d="M0 3h16v10H0z"/><path d="M0 3l8 6 8-6" stroke="#f3f3f3" stroke-width="1.2" fill="none"/></svg>opartridge65@mailbox.com</div>
  <div class="abs contact-row" style="top:722px;"><svg viewBox="0 0 16 16"><path d="M3 1l3 3-2 2c1 2 3 4 5 5l2-2 3 3-2 3C7 15 1 9 1 3z"/></svg>(555) 014-2276</div>
  <div class="abs contact-row" style="top:739px;"><svg viewBox="0 0 16 16"><rect x="1" y="1" width="14" height="14"/></svg>@opartridge65</div>
  <div class="abs contact-row" style="top:755px;"><svg viewBox="0 0 16 16" fill="none" stroke="#3a3d41" stroke-width="1.1"><circle cx="8" cy="8" r="6.5"/><ellipse cx="8" cy="8" rx="3" ry="6.5"/><path d="M1.5 8h13M2.5 4.5h11M2.5 11.5h11"/></svg>opartridge.com</div>

  <div class="abs footer-bar"></div>
</main>
</body>
</html>
```